Web design for construction/ handyman company. We are a new company and trying to brand ourselves.

We have a logo with a character already in place and want a user friendly and simple site. I'm attaching our logo designs with our Crocodile character to get an idea of our logo. We want people to remember us and our site. The name we chose was so we could use a logo with a character. Our name is Pelican Builders LLC.

Target Market(s)

New clients

Industry/Entity Type

Contractor

Coding

Coded - Design and coding required

Number of Pages Required

4 page

Font styles to use
Sans Serif

Requirements
Must have
• About Us Page, What we do (not sure what to call this), Contact Us, Home Page. Would like the same colors as on our business card designs to be used on the website.
Nice to have
• We eventually want a project page to add photos of projects but thats not necessary now. Would be nice to use the crocodile theme, hammer or something similar somehow in the page names or clicks.

```html
<!DOCTYPE html>
<html lang="en">
<head>
<meta charset="utf-8">
<title>Pelican Builders LLC</title>
<link href="https://fonts.googleapis.com/css2?family=Open+Sans:wght@400;600;700&display=swap" rel="stylesheet">
<style>
:root{
  --green:#5aab1e;
  --green-dark:#3f8512;
  --navy:#1b3463;
  --navy-deep:#132749;
  --blue:#1f62ad;
  --ink:#333;
  --muted:#777;
  --paper:#fff;
  --mist:#eef0f2;
}
*{box-sizing:border-box;margin:0;padding:0}
html,body{width:675px;height:1200px;overflow:hidden;background:var(--paper)}
body{font-family:"Open Sans",Arial,sans-serif;color:var(--ink);font-size:7px;line-height:1.35}
.btn{display:inline-block;background:var(--green);color:#fff;font-size:7px;padding:4px 12px;border-radius:3px;text-decoration:none}

/* header */
.site-header{height:63px;display:flex;align-items:center;padding:0 30px 0 70px;position:relative}
.brand{display:flex;align-items:center;gap:6px;font-weight:700;font-size:11px;color:var(--green-dark)}
.brand-mark{width:14px;height:14px;border-radius:50%;background:var(--green)}
.main-nav{display:flex;gap:14px;margin-left:38px;margin-top:22px}
.main-nav a{font-size:8.5px;color:var(--ink);text-decoration:none}
.main-nav a.active{color:var(--green);border-bottom:2px solid var(--green)}
.social{position:absolute;right:30px;top:8px;display:flex;gap:5px}
.social span{width:14px;height:14px;border-radius:50%;border:1px solid #999}

/* hero */
.hero{height:162px;position:relative;background:linear-gradient(100deg,#d9b735 0 12%,#7d8a98 28%,#9fb5c9 60%,#c7d6e4 100%);text-align:center;color:#fff}
.hero h1{padding-top:50px;font-size:17px;font-weight:700}
.hero p{width:260px;margin:4px auto 8px;font-size:6.5px}

/* services */
.services{height:265px;background:var(--mist);position:relative;padding:35px 48px 0}
.divider{position:absolute;left:0;width:675px;height:3px;background:var(--green)}
.divider.top{top:0}.divider.bottom{bottom:0}
.service-list{display:flex;justify-content:space-between}
.service-card{width:106px;text-align:center}
.service-shape{height:160px;background:#8a8f96;clip-path:polygon(0 0,100% 0,100% 74%,50% 100%,0 74%);position:relative;color:#fff;padding:14px 6px 0;text-align:left}
.service-shape h3{font-size:8px;color:#fff;font-weight:700;margin-bottom:3px}
.service-shape p{font-size:5.5px}
.service-card .btn{margin-top:-8px;position:relative}
.s1{background:linear-gradient(#6d7e8c,#c3a58a)}
.s2{background:linear-gradient(#6c8fb6,#3e5067)}
.s3{background:linear-gradient(#a7b9c9,#6f7883)}
.s4{background:linear-gradient(#9aa7b8,#6b5a4d)}
.s5{background:linear-gradient(#c4c8c5,#7a8074)}

/* about */
.about{height:180px;background:linear-gradient(90deg,#5e7180 0%,#8a9aa6 45%,#c9b48f 75%,#b7bfc6 100%);color:#fff;position:relative}
.about-copy{position:absolute;left:178px;top:30px;width:300px;text-align:center}
.about-copy h2{font-size:19px;font-weight:700;margin-bottom:8px}
.about-copy p{font-size:6px;margin-bottom:10px}

/* features */
.features{height:165px;display:flex;justify-content:space-between;padding:22px 48px 0}
.feature{width:100px}
.feature-icon{width:36px;height:36px;background:var(--blue);margin:0 auto 8px}
.feature h3{color:var(--blue);font-size:8px;font-weight:700}
.feature p{font-size:5.5px;color:var(--muted);margin:3px 0 6px}
.feature .btn{padding:3px 9px;font-size:6px}

/* cta */
.cta{height:150px;background:linear-gradient(160deg,#dfe3e6 0%,#c9ccd0 45%,#e3c24a 60%,#b5b9bd 100%);text-align:center;position:relative}
.cta h2{padding-top:42px;font-size:15px;font-weight:400;color:#fff;line-height:1.3}
.cta .btn{margin-top:10px}

/* newsletter */
.newsletter{height:102px;background:linear-gradient(#3e3e3e,#555 60%,#777);text-align:center;color:#fff;padding-top:20px}
.newsletter h3{font-size:8px;font-weight:700;line-height:1.4}
.signup{display:flex;justify-content:center;margin-top:14px}
.signup span{width:405px;height:22px;background:#fff;border-radius:3px 0 0 3px;color:var(--green);font-size:7px;text-align:left;padding:6px 10px}
.signup b{width:78px;height:22px;background:var(--green);border-radius:0 3px 3px 0;font-size:8px;padding-top:5px}

/* footer */
.site-footer{height:113px;background:var(--navy);color:#fff;position:relative}
.footer-cols{display:flex;padding:18px 0 0 48px}
.footer-col{width:120px}
.footer-col h4{font-size:8px;font-weight:700;margin-bottom:6px}
.footer-col li{list-style:none;font-size:6px;line-height:1.45;color:#d6deeb}
.mascot{position:absolute;right:14px;top:8px;width:70px;height:84px;border-radius:8px;background:linear-gradient(#4f9a3f,#2f6f2e)}
.copyright{position:absolute;bottom:0;left:0;right:0;height:14px;background:var(--navy-deep);text-align:center;font-size:5.5px;padding-top:3px;color:#c6cfdd}
</style>
</head>
<body>
<header class="site-header">
  <div class="brand"><span class="brand-mark"></span>Pelican Builders</div>
  <nav class="main-nav">
    <a class="active" href="#">Home</a><a href="#">About us</a><a href="#">Locations</a><a href="#">Product</a><a href="#">Client</a><a href="#">Contact us</a><a href="#">FAQ</a><a href="#">Blog</a>
  </nav>
  <div class="social"><span></span><span></span><span></span><span></span></div>
</header>

<section class="hero" role="img" aria-label="Photo of a construction worker holding a yellow hard hat in front of a building site">
  <h1>Create!</h1>
  <p>Lorem ipsum dolor sit amet, consectetur adipiscing elit. Praesent facilisis lectus ut nibh, sed viverra nunc tempor eget.</p>
  <a class="btn" href="#">Click Here</a>
</section>

<section class="services">
  <div class="divider top"></div>
  <div class="service-list">
    <article class="service-card"><div class="service-shape s1" role="img" aria-label="Photo of a handshake on a job site"><h3>Lorem Ipsum</h3><p>Lorem ipsum is that it has a more normal distribution of letters, as opposed to using content here.</p></div><a class="btn" href="#">Click Here</a></article>
    <article class="service-card"><div class="service-shape s2" role="img" aria-label="Photo of solar panels on a roof"><h3>Lorem Ipsum</h3><p>Lorem ipsum is that it has a more normal distribution of letters, as opposed to using content here.</p></div><a class="btn" href="#">Click Here</a></article>
    <article class="service-card"><div class="service-shape s3" role="img" aria-label="Photo of a tall building under construction"><h3>Lorem Ipsum</h3><p>Lorem ipsum is that it has a more normal distribution of letters, as opposed to using content here.</p></div><a class="btn" href="#">Click Here</a></article>
    <article class="service-card"><div class="service-shape s4" role="img" aria-label="Photo of a modern building facade"><h3>Lorem Ipsum</h3><p>Lorem ipsum is that it has a more normal distribution of letters, as opposed to using content here.</p></div><a class="btn" href="#">Click Here</a></article>
    <article class="service-card"><div class="service-shape s5" role="img" aria-label="Photo of a concrete structure"><h3>Lorem Ipsum</h3><p>Lorem ipsum is that it has a more normal distribution of letters, as opposed to using content here.</p></div><a class="btn" href="#">Click Here</a></article>
  </div>
  <div class="divider bottom"></div>
</section>

<section class="about" role="img" aria-label="Photo of a smiling builder in a white hard hat">
  <div class="about-copy">
    <h2>What We Are</h2>
    <p>There are many variations of passages of Lorem Ipsum available, but the majority have suffered alteration in some form, by injected humour, or randomised words which don't look even slightly believable. If you are going to use a passage of Lorem Ipsum, you need to be sure there isn't anything hidden in the middle of text.</p>
    <a class="btn" href="#">Learn More</a>
  </div>
</section>

<section class="features">
  <article class="feature"><div class="feature-icon" role="img" aria-label="Hazard sign icon"></div><h3>Lorem Ipsum</h3><p>There are many variations of passages of Lorem Ipsum available, but some.</p><a class="btn" href="#">Get More</a></article>
  <article class="feature"><div class="feature-icon" role="img" aria-label="Road barrier icon"></div><h3>Lorem Ipsum</h3><p>There are many variations of passages of Lorem Ipsum available, but some.</p><a class="btn" href="#">Get More</a></article>
  <article class="feature"><div class="feature-icon" role="img" aria-label="Worker with shovel icon"></div><h3>Lorem Ipsum</h3><p>There are many variations of passages of Lorem Ipsum available, but some.</p><a class="btn" href="#">Get More</a></article>
  <article class="feature"><div class="feature-icon" role="img" aria-label="Hard hat icon"></div><h3>Lorem Ipsum</h3><p>There are many variations of passages of Lorem Ipsum available, but some.</p><a class="btn" href="#">Get More</a></article>
  <article class="feature"><div class="feature-icon" role="img" aria-label="Paint roller icon"></div><h3>Lorem Ipsum</h3><p>There are many variations of passages of Lorem Ipsum available, but some.</p><a class="btn" href="#">Get More</a></article>
</section>

<section class="cta" role="img" aria-label="Photo of a yellow tape measure on building blueprints">
  <h2>We are ready to satisfy all your<br>project requirements!</h2>
  <a class="btn" href="#">Learn More</a>
</section>

<section class="newsletter">
  <h3>Interested in Our Offers?<br>Fill This Form And We Will Get You</h3>
  <div class="signup"><span>Email</span><b>Submit</b></div>
</section>

<footer class="site-footer">
  <div class="footer-cols">
    <div class="footer-col"><h4>Products</h4><ul><li>Vestibulum</li><li>Cras iaculis</li><li>Fusce ornare</li><li>Fusce euismod</li><li>Consequat</li><li>Adipiscing elit</li></ul></div>
    <div class="footer-col"><h4>Technology</h4><ul><li>Nulla eros nulla</li><li>Tellus arcu</li></ul></div>
    <div class="footer-col"><h4>Company</h4><ul><li>Home</li><li>About us</li><li>Projects</li><li>Blog</li><li>Contacts</li></ul></div>
    <div class="footer-col"><h4>Contact</h4><ul><li>Telephone: +1 555-0100</li><li>FAX: +1 555-0101</li><li>E-mail: hello@pelicanbuilders.example</li></ul></div>
  </div>
  <div class="mascot" role="img" aria-label="Company mascot character illustration"></div>
  <div class="copyright">Pelican Builders LLC © 2015 Privacy Policy</div>
</footer>
</body>
</html>
```